Substance abuse awareness flyer for school age kids

I am needing a flyer for school-age kids. What if it were designed to look like an Voxtab with someone texting and the text bubbles were some of the text below with emojis? Maybe a text chain between to friends:

Maybe the first text bubble says "I'm thinking about using drugs and alcohol"
the next bubble: "Just say no!" ( perhaps a stop sign emoji ?)

"Talk to your parents, your teachers at school, or your doctor about how drugs and alcohol can harm you"

another text bubble "did you know that alcohol and drugs could lead to..."
then include some of the info below (see links for more info).
Where ever you get info, it must be cited.

this needs to be English on one side and Spanish on the other side and needs to include the logo attached.

The effects of substance abuse
BHW: https://www.bhwagency.org/youth/features/teen-substance-use.html
Affect growth and development, especially brain development. Not able to focus at school or be around friends. https://www.kestrowline.org/sites/default/files/preventingdruguse_2.pdf
Leads to risky behaviors and lack of impulse control (dangerous activities) https://www.kestrowline.org/sites/default/files/preventingdruguse_2.pdf
Contribute to health problems as an adult: heart disease, high blood pressure, and trouble sleeping.

Target Market(s)

school age kids 9-20

Requirements
Must have
• Print ready: 8.5x11

```html
<!DOCTYPE html>
<html lang="en">
<head>
<meta charset="utf-8">
<title>Substance Abuse Awareness Flyer</title>
<link href="https://fonts.googleapis.com/css2?family=Lato:wght@400;700;900&display=swap" rel="stylesheet">
<style>
  :root{
    --maroon:#5e2333;
    --maroon-deep:#3a1119;
    --coral:#ee4a4a;
    --pink:#f0566e;
    --orange:#f27a5a;
    --sky:#e3f1f9;
    --blue:#1b66b5;
    --navy:#1f2a5c;
    --skin:#f39a92;
    --ink:#111111;
    --white:#ffffff;
  }
  *{margin:0;padding:0;box-sizing:border-box}
  html,body{width:974px;height:1200px;overflow:hidden;background:#fff}
  body{font-family:'Lato',sans-serif}
  .flyer{position:relative;width:974px;height:1200px;overflow:hidden;background:var(--white)}
  .backdrop{position:absolute;inset:0}
  .illustration{position:absolute;left:60px;top:40px;width:560px;height:830px;border-radius:40px;
    background:linear-gradient(160deg,#b7cbe6 0%,var(--navy) 35%,#2b3a78 55%,var(--skin) 80%,#f6b3ab 100%);opacity:.9}
  .headline{position:absolute;right:38px;top:74px;width:360px;text-align:right;color:var(--white);
    font-weight:700;font-size:27px;line-height:32px}
  .bubble{position:absolute;color:var(--white);font-weight:700}
  .bubble svg{position:absolute;inset:0;overflow:visible}
  .bubble span{position:relative;display:block}
  .bubble-ask{left:65px;top:205px;width:370px;height:160px;font-size:29px;line-height:35px}
  .bubble-ask span{padding:27px 0 0 56px}
  .bubble-no{left:308px;top:402px;width:180px;height:100px;font-size:27px;line-height:33px}
  .bubble-no span{padding:16px 0 0 34px}
  .stop{display:inline-block;vertical-align:-4px;margin-left:6px}
  .bubble-empty{left:88px;top:513px;width:303px;height:92px}
  .bubble-know{left:606px;top:760px;width:330px;height:172px;font-size:27px;line-height:34px}
  .bubble-know span{padding:30px 0 0 44px}
  .brand{position:absolute;left:631px;top:284px;width:300px;height:300px;border-radius:50%;
    border:3px solid #3aa3e0;background:var(--white);display:flex;align-items:center;justify-content:center;
    text-align:center;color:var(--maroon);font-weight:900;font-size:30px;line-height:36px;padding:40px}
  .info{position:absolute;left:53px;top:952px;width:900px;color:var(--ink)}
  .info h2{font-size:23px;font-weight:900;color:var(--maroon);margin-bottom:8px}
  .info p{font-size:16px;line-height:22px}
  .info a{display:block;font-size:18px;line-height:22px;color:var(--maroon);text-decoration:none;margin-bottom:8px}
  .footer{position:absolute;left:0;right:0;bottom:0;height:57px;background:linear-gradient(90deg,var(--maroon),var(--maroon-deep));
    color:var(--white);font-size:17.5px;padding:16px 0 0 53px}
</style>
</head>
<body>
<main class="flyer">
  <svg class="backdrop" width="974" height="1200" viewBox="0 0 974 1200" aria-hidden="true">
    <rect width="974" height="900" fill="var(--sky)"/>
    <path d="M0 0 H300 C290 80 240 120 140 130 L0 130 Z" fill="var(--blue)"/>
    <path d="M270 0 H974 V255 C820 300 640 280 560 230 C450 170 390 150 330 60 Z" fill="var(--maroon)"/>
    <path d="M0 870 C300 940 650 900 974 810 V900 C650 1000 300 1020 0 950 Z" fill="var(--white)"/>
    <path d="M0 878 C300 948 650 905 974 812 V828 C650 925 300 965 0 900 Z" fill="var(--maroon)"/>
    <rect y="900" width="974" height="300" fill="#f7f7f9"/>
    <path d="M0 905 C300 975 650 930 974 835 V910 L0 910 Z" fill="var(--white)"/>
  </svg>

  <div class="illustration" role="img" aria-label="Illustration of two hands holding a smartphone and typing a text conversation"></div>

  <p class="headline">Talk to your parents, your teachers at school, or your doctor about how drugs and alcohol can harm you.</p>

  <div class="bubble bubble-ask">
    <svg width="370" height="160" aria-hidden="true"><path d="M40 0 H330 A40 40 0 0 1 370 40 V120 A40 40 0 0 1 330 160 H250 L262 205 L210 160 H40 A40 40 0 0 1 0 120 V40 A40 40 0 0 1 40 0 Z" fill="var(--coral)"/></svg>
    <span>I'm thinking about<br>using drugs and<br>alcohol</span>
  </div>

  <div class="bubble bubble-no">
    <svg width="180" height="100" aria-hidden="true"><defs><linearGradient id="noGrad" x1="0" x2="1"><stop offset="0" stop-color="var(--orange)"/><stop offset="1" stop-color="var(--pink)"/></linearGradient></defs><path d="M35 0 H145 A35 35 0 0 1 180 35 V65 A35 35 0 0 1 145 100 H135 L137 120 L110 100 H35 A35 35 0 0 1 0 65 V35 A35 35 0 0 1 35 0 Z" fill="url(#noGrad)"/></svg>
    <span>Just say<br>NO!<svg class="stop" width="26" height="26" viewBox="0 0 26 26" aria-hidden="true"><polygon points="8,1 18,1 25,8 25,18 18,25 8,25 1,18 1,8" fill="#d62828" stroke="#fff" stroke-width="1.5"/><rect x="6" y="11.5" width="14" height="3" fill="#fff"/></svg></span>
  </div>

  <div class="bubble bubble-empty">
    <svg width="303" height="92" aria-hidden="true"><path d="M40 0 H263 A40 40 0 0 1 303 40 V52 A40 40 0 0 1 263 92 H235 L232 115 L200 92 H40 A40 40 0 0 1 0 52 V40 A40 40 0 0 1 40 0 Z" fill="var(--coral)"/></svg>
  </div>

  <div class="brand">Riverbend Care Network</div>

  <div class="bubble bubble-know">
    <svg width="330" height="172" aria-hidden="true"><path d="M30 0 H300 A30 30 0 0 1 330 30 V142 A30 30 0 0 1 300 172 H110 L34 218 L60 172 H30 A30 30 0 0 1 0 142 V30 A30 30 0 0 1 30 0 Z" fill="var(--maroon-deep)"/></svg>
    <span>did you know that<br>alcohol and drugs<br>could lead to...</span>
  </div>

  <section class="info">
    <h2>FOR MORE INFORMATION:</h2>
    <p>The effects of substance abuse BHW:</p>
    <a href="https://www.bhwagency.org/youth/features/teen-substance-use.html">https://www.bhwagency.org/youth/features/teen-substance-use.html</a>
    <p>Affect growth and development, especially brain development. Not able to focus at school or be around friends.</p>
    <a href="https://www.kestrowline.org/sites/default/files/preventingdruguse_2.pdf">https://www.kestrowline.org/sites/default/files/preventingdruguse_2.pdf</a>
    <p>Leads to risky behaviors and lack of impulse control (dangerous activities)</p>
    <a href="https://www.kestrowline.org/sites/default/files/preventingdruguse_2.pdf">https://www.kestrowline.org/sites/default/files/preventingdruguse_2.pdf</a>
  </section>

  <footer class="footer">Contribute to health problems as an adult: heart disease, high blood pressure, and trouble sleeping.</footer>
</main>
</body>
</html>
```